New Website Design (Uncoded) Competition for Lorvex Trade Link

Please submit design concepts for a Joomla 3.0 Website for LORVEX TRADE LINK company. Our client prefers a modem style design, responsive to all mobile devices,
The website demo content needs to be clear and detailed.

Menu sample:
Home/About Us/Service/Strength/Partner/News/Contact US/Blog

Requirements:
1. Only need to submit the PSD for the design, coding work is not included.
2. Please submit both Homepage and Inner page to demonstrate the concept.
3. The Homepage needs to include: LOGO/MENU/Banner/Language Switcher/Company Introduction/Welcome module/Advertising Module/Footer Menu/Footer/Copyright/Social Links
4. Use Asian business women for demo pictures/Could try city pictures for background.
5. Prefer SINGLE SCREEN design rather than scrollable multiple screen designs.
6. Avoid any chain symbol since the company is more about financial business.
7. Avoid any direct connotations related with money or cash.
Updates

Hi Designers, I have clearly state the requirements that avoid using neg connontation pictures like cash/ property, though still receive concepts like that. Please check the brief clearly and mark at Update with "cheers" Kel from VT

Target Market(s)

Dongrui Lorvex Trade link Company provide cross-border Supply chain Financial service by integrating Dongrui Trade Link resource.
The Company mission is become the most respectful, professional and valuable Chinese Supply Chain Financial Company, pioneer the supply chain industry.

Industry/Entity Type

Financial

Font styles to use
Sans Serif

Colors
33b7a4

Requirements
Must have
• 1. Necessary Web element, including Logo/navigation/ Banner/ Footer
2. Asia business Women pictures.
Should not have
• 6. Avoid any chain symbol since the company is more about financial business.

```html
<!DOCTYPE html>
<html lang="en">
<head>
<meta charset="utf-8">
<title>Lorvex Trade Link</title>
<link rel="stylesheet" href="https://fonts.googleapis.com/css2?family=Arimo:wght@400;700&family=Lato:wght@300;400;700&family=Oswald:wght@500&family=Tinos&display=swap">
<style>
:root{
  --blue:#1e7bc4;
  --teal:#33b7a4;
  --ink:#444;
  --muted:#666;
  --line:#dcdcdc;
  --card-band:#e6e6e6;
  --footer:#555;
  --slate:rgba(80,86,96,.85);
}
*{margin:0;padding:0;box-sizing:border-box}
html,body{width:1147px;height:1200px;overflow:hidden;background:#fff}
body{position:relative;font-family:Arimo,Arial,sans-serif;color:var(--ink)}
.abs{position:absolute}
.topbar{left:0;top:0;width:1147px;height:34px;background:var(--blue)}
.topbar .call{position:absolute;right:134px;top:8px;font-size:15px;color:var(--teal);display:flex;align-items:center;gap:6px}
.topbar .call b{color:#fff;margin-left:4px;font-size:16px}
.brand{left:96px;top:72px;display:flex;align-items:center;gap:12px}
.brand .mark{width:30px;height:30px;background:var(--blue)}
.brand .name{font-family:Lato,sans-serif;font-weight:700;font-size:31px;color:#555;letter-spacing:1px}
.lang{left:756px;top:75px;width:211px;height:30px;border:1px solid var(--line);border-radius:3px;background:#fafafa;display:flex;align-items:center;padding:0 7px 0 10px;font-size:12px;color:#555}
.lang .flag{width:28px;height:17px;margin-right:12px;display:flex;flex-direction:column}
.lang .flag i{flex:1}
.lang .arrow{margin-left:auto;width:20px;height:20px;border:1px solid #ccc;background:#eee;display:flex;align-items:center;justify-content:center}
.mainnav{left:0;top:166px;width:1147px;height:42px;border-top:1px solid var(--line);border-bottom:2px solid #e4e4e4}
.mainnav a{position:absolute;top:13px;font-size:13px;color:#333;text-decoration:none}
.mainnav a.active{color:var(--teal)}
.hero{left:0;top:208px;width:1147px;height:489px;background:linear-gradient(180deg,#c9c2bb 0%,#e6cdb0 30%,#d9c4ad 50%,#b7aea6 75%,#a8a29f 100%)}
.hero .person{position:absolute;left:96px;top:28px;width:395px;height:461px;background:linear-gradient(180deg,#6b4a3c 0%,#3a3433 55%,#2b2b2e 100%);border-radius:180px 180px 0 0;opacity:.55}
.hero h1{position:absolute;left:579px;top:222px;font-family:Tinos,serif;font-weight:400;font-size:37px;color:#fff;letter-spacing:.5px}
.hero .sub{position:absolute;left:540px;top:276px;width:485px;height:55px;background:var(--slate);font-family:Oswald,sans-serif;font-size:28px;color:#fff;display:flex;align-items:center;justify-content:center}
.hero .sub em{font-style:normal;color:var(--teal);margin-left:9px}
.hero .btn{position:absolute;left:673px;top:349px;width:195px;height:45px;background:var(--teal);color:#fff;font-size:17px;display:flex;align-items:center;justify-content:center;gap:16px}
.hero .btn span.go{width:29px;height:24px;background:var(--blue);display:flex;align-items:center;justify-content:center}
.card{top:739px;width:255px;height:256px;border:1px solid var(--line);background:linear-gradient(180deg,#f1f1f1 0%,#fff 45%);text-align:center}
.card .icon{margin:30px auto 0;width:48px;height:48px}
.card h2{font-family:Lato,sans-serif;font-weight:400;font-size:22px;color:#444;margin-top:12px}
.card h2 span{color:var(--teal)}
.card p{font-size:13px;line-height:17px;color:var(--muted);margin:11px 14px 0}
.card .more{position:absolute;left:1px;right:1px;bottom:1px;height:31px;background:var(--card-band);font-size:13px;color:#555;display:flex;align-items:center;justify-content:center;gap:8px}
.card .more b{color:var(--teal)}
.strip{left:0;top:1036px;width:1147px;height:8px;background:#e4e4e4}
.footnav{left:0;top:1044px;width:1147px;height:42px;background:var(--blue)}
.footnav a{position:absolute;top:0;height:42px;display:flex;align-items:center;justify-content:center;font-size:13px;color:#fff;text-decoration:none}
.footnav a+a{border-left:2px solid #fff}
.footer{left:0;top:1086px;width:1147px;height:114px;background:var(--footer)}
.footer p{position:absolute;top:28px;width:100%;text-align:center;font-size:13px;color:#fff}
.social{position:absolute;top:63px;left:502px;display:flex;gap:6px}
.social i{width:32px;height:32px;border-radius:50%;background:#333;display:block}
</style>
</head>
<body>
<div class="abs topbar">
  <div class="call">
    <svg width="18" height="18" viewBox="0 0 18 18"><circle cx="9" cy="9" r="9" fill="#33b7a4"/><path d="M6 4.5l1.6 2.2-1 1.2c.6 1.3 1.6 2.3 2.9 2.9l1.2-1 2.2 1.6-.8 1.7c-3.7-.2-6.8-3.3-7-7z" fill="#fff"/></svg>
    Call us now !! <b>08 5512 7708</b>
  </div>
</div>

<div class="abs brand"><span class="mark"></span><span class="name">LORVEX TRADE LINK</span></div>

<div class="abs lang">
  <span class="flag"><i style="background:#000"></i><i style="background:#d00"></i><i style="background:#fc0"></i></span>
  Select your Language
  <span class="arrow"><svg width="10" height="6" viewBox="0 0 10 6"><path d="M0 0h10L5 6z" fill="#1e7bc4"/></svg></span>
</div>

<nav class="abs mainnav">
  <a class="active" style="left:106px">HOME</a>
  <a style="left:195px">ABOUT US</a>
  <a style="left:310px">SERVICE</a>
  <a style="left:416px">STRENGTH</a>
  <a style="left:536px">PARTNER</a>
  <a style="left:646px">NEWS</a>
  <a style="left:735px">CONTACT US</a>
  <a style="left:866px">BLOG</a>
</nav>

<section class="abs hero" role="img" aria-label="Smiling Asian business woman in a dark suit in front of a city skyline at sunset">
  <div class="person"></div>
  <h1>LOREM IPSUM DOLOR</h1>
  <div class="sub">SED UT PERSPICIATIS UNDE <em>TOTAM</em></div>
  <div class="btn">READ MORE <span class="go"><svg width="8" height="12" viewBox="0 0 8 12"><path d="M1 1l5 5-5 5" stroke="#fff" stroke-width="2" fill="none"/></svg></span></div>
</section>

<article class="abs card" style="left:135px">
  <svg class="icon" viewBox="0 0 48 48"><circle cx="20" cy="24" r="17" fill="#333"/><circle cx="20" cy="24" r="8" fill="#33b7a4"/><circle cx="38" cy="30" r="8" fill="#555"/><circle cx="38" cy="30" r="3" fill="#33b7a4"/></svg>
  <h2>Our <span>Introduction</span></h2>
  <p>Dolore magna aliqua. Ut enim ad minim veniam, quis nostrud exercita-tion ullamco laboris nisi ut aliquip ex ea commodo consequat</p>
  <div class="more">READ MORE <b>››</b></div>
</article>

<article class="abs card" style="left:421px">
  <svg class="icon" viewBox="0 0 48 48"><circle cx="10" cy="12" r="4" fill="#33b7a4"/><rect x="6" y="17" width="8" height="20" fill="#33b7a4"/><circle cx="38" cy="12" r="4" fill="#33b7a4"/><rect x="34" y="17" width="8" height="20" fill="#33b7a4"/><circle cx="24" cy="16" r="4" fill="#222"/><rect x="20" y="21" width="8" height="22" fill="#222"/></svg>
  <h2>Welcome <span>To Our Site</span></h2>
  <p>Dolore magna aliqua. Ut enim ad minim veniam, quis nostrud exercita-tion ullamco laboris nisi ut aliquip ex ea commodo consequat</p>
  <div class="more">READ MORE <b>››</b></div>
</article>

<article class="abs card" style="left:707px">
  <svg class="icon" viewBox="0 0 48 48"><circle cx="24" cy="24" r="23" fill="none" stroke="#9fe0d6"/><circle cx="24" cy="24" r="18" fill="#33b7a4"/><circle cx="24" cy="24" r="12" fill="#1f4f5a"/></svg>
  <h2>Advertisement <span>Module</span></h2>
  <p>Dolore magna aliqua. Ut enim ad minim veniam, quis nostrud exercita-tion ullamco laboris nisi ut aliquip ex ea commodo consequat</p>
  <div class="more">READ MORE <b>››</b></div>
</article>

<div class="abs strip"></div>
<nav class="abs footnav">
  <a style="left:100px;width:98px">HOME</a>
  <a style="left:198px;width:123px">ABOUT US</a>
  <a style="left:321px;width:109px">SERVICE</a>
  <a style="left:430px;width:135px">STRENGTH</a>
  <a style="left:565px;width:122px">PARTNER</a>
  <a style="left:687px;width:104px">NEWS</a>
  <a style="left:791px;width:140px">CONTACT US</a>
  <a style="left:931px;width:100px">BLOG</a>
</nav>

<footer class="abs footer">
  <p>Copyright © 2014 All Rights Reserved | Privacy Policy</p>
  <div class="social"><i></i><i></i><i></i><i></i></div>
</footer>
</body>
</html>
```